Print & Packaging Design for Snug Pip Teething & Healing Necklaces

Bring your Creative Juices this-a way! Smart, savvy, up-market business needs a logo & swing tags! Do you have what it takes?

```html
<!DOCTYPE html>
<html lang="en">
<head>
<meta charset="utf-8">
<title>Snug Pip – Swing Tag</title>
<link rel="stylesheet" href="https://fonts.googleapis.com/css2?family=Quicksand:wght@500;600&family=Archivo+Narrow:wght@700&display=swap">
<style>
  :root {
    --page: #ffffff;
    --ink: #231f20;
    --plum: #6a5a8c;
    --cream: #fffaeb;
    --butter: #fbe6a8;
    --gold: #f3cd6e;
    --frame: #f6d84e;
    --photo-light: #f1efec;
    --photo-dark: #d9d2c6;
    --hole: #ffffff;
  }
  html, body {
    margin: 0;
    padding: 0;
    width: 1200px;
    height: 1131px;
    overflow: hidden;
    background: var(--page);
  }
  .canvas { display: block; width: 1200px; height: 1131px; }
  .side-label {
    font-family: "Archivo Narrow", "Arial Narrow", sans-serif;
    font-weight: 700;
    font-size: 32px;
    fill: var(--ink);
  }
  .side-underline { stroke: var(--ink); stroke-width: 2.5; }
  .brand-name {
    font-family: "Quicksand", sans-serif;
    font-weight: 500;
    fill: var(--plum);
  }
  .brand-name--front { font-size: 118px; }
  .brand-name--back { font-size: 78px; }
  .tagline {
    font-family: "Quicksand", sans-serif;
    font-weight: 500;
    fill: var(--plum);
  }
  .tagline--front { font-size: 33px; }
  .tagline--back { font-size: 22px; }
  .benefits {
    font-family: "Quicksand", sans-serif;
    font-weight: 500;
    font-size: 22px;
    fill: var(--plum);
  }
  .tag-shape { stroke: none; }
  .punch-hole { fill: var(--hole); stroke: var(--ink); stroke-width: 1.5; stroke-dasharray: 4 3; }
  .photo-frame { stroke: var(--frame); stroke-width: 7; }
</style>
</head>
<body>
<svg class="canvas" viewBox="0 0 1200 1131" xmlns="http://www.w3.org/2000/svg">
  <defs>
    <radialGradient id="tagFill" cx="0.42" cy="0.55" r="0.65">
      <stop offset="0" stop-color="var(--cream)"/>
      <stop offset="0.45" stop-color="var(--butter)"/>
      <stop offset="1" stop-color="var(--gold)"/>
    </radialGradient>
    <radialGradient id="photoFill" cx="0.5" cy="0.45" r="0.6">
      <stop offset="0" stop-color="var(--photo-light)"/>
      <stop offset="1" stop-color="var(--photo-dark)"/>
    </radialGradient>
  </defs>

  <!-- Front side -->
  <g class="tag tag--front">
    <text class="side-label" x="577" y="44" text-anchor="middle">Front</text>
    <line class="side-underline" x1="536" y1="50" x2="618" y2="50"/>

    <path class="tag-shape" fill="url(#tagFill)"
      d="M59,370 C59,300 150,250 250,240 C280,170 360,140 430,140 C480,80 600,65 700,72 C760,60 850,70 900,100 C1000,110 1090,170 1110,250 C1160,290 1184,330 1184,380 C1184,480 1000,555 620,555 C250,555 59,470 59,370 Z"/>

    <circle class="punch-hole" cx="101" cy="363" r="27"/>

    <ellipse class="photo-frame" cx="913" cy="281" rx="166" ry="111" fill="url(#photoFill)"
      role="img" aria-label="Photo of a smiling baby in a striped beanie wearing an amber teething necklace"/>

    <text class="brand-name brand-name--front" x="445" y="345" text-anchor="middle">Snug Pip</text>
    <text class="tagline tagline--front" x="777" y="468" text-anchor="middle">- Teething &amp; Healing Necklaces -</text>
  </g>

  <!-- Back side -->
  <g class="tag tag--back">
    <text class="side-label" x="577" y="620" text-anchor="middle">Back</text>
    <line class="side-underline" x1="540" y1="626" x2="614" y2="626"/>

    <path class="tag-shape" fill="url(#tagFill)"
      d="M59,950 C59,860 130,800 250,790 C320,760 380,740 430,735 C450,680 560,651 700,652 C850,655 950,690 960,745 C1080,760 1184,830 1184,920 C1184,1060 1000,1125 620,1125 C230,1125 59,1040 59,950 Z"/>

    <circle class="punch-hole" cx="1095" cy="929" r="27"/>

    <text class="brand-name brand-name--back" x="296" y="935" text-anchor="middle">Snug Pip</text>
    <text class="tagline tagline--back" x="296" y="1030" text-anchor="middle">- Teething &amp; Healing Necklaces -</text>

    <text class="benefits" text-anchor="middle">
      <tspan x="755" y="777">• natural pain relief for your babe</tspan>
      <tspan x="755" y="814">• relieve your babes pain and sleep better at night</tspan>
      <tspan x="755" y="851">• sleep better at night knowing you've helped to</tspan>
      <tspan x="755" y="880">ease your babes pain</tspan>
      <tspan x="755" y="919">• baltic amber teething necklaces</tspan>
      <tspan x="755" y="958">• gemstone nursing necklaces</tspan>
      <tspan x="755" y="998">• fertility and birthing jewellery</tspan>
      <tspan x="755" y="1038">• natural healing jewellery</tspan>
    </text>
  </g>
</svg>
</body>
</html>
```